Tidecrest NZ Brand, Revenue, Promotions & Events

I need an innovative business card that pops my brand. I like the colours against darker gradients and i'm not afraid to be bold.

I run my own Business, Brand, Event & Promotion company. I specialise in breathing life into businesses and adding atmosphere to promotions and events. I am concept based lady that likes to test the boundaries and create stand out campaigns that connect with the consumer.

I have 12 years business experience in a realm of interesting fields form 11 years in coordinating international music festivals & promotions, 6 years in radio with 8 radio awards including a NZ radio award for best sales team in NZ and was the national brand and sales manager for New Zealands 1st indoor entertainment mall. With 10 years of experience in advertising sales, I have an eye for creating revenue streams for businesses and thrive on implementing campaigns that compliment those streams.

I love sayings like "Do what you love, love what you do" and believe that you can achieve anything you want.

I have been fortunate in my career that my connections have carried me without needing to promote my business however it is important that I start to do so.

Target Market(s)

Decision makers 25 to 54

Contact Information for Business Card

Petra Ollingham
Director
p. 022 587 3091
e. petra@tidecrest.nz
www.tidecrest.nz

FB, IG and Linkedin logo

Font styles to use
Sans Serif

Colors

Designer to choose colors to be used in the design.

Requirements
Must have
• Petra Ollingham
• Director
• p. 022 587 3091
• e. petra@tidecrest.nz
• www.tidecrest.nz
• FB, IG and Linkedin logo
Nice to have
• I am looking for a business card with character, that leaves my presence with my customer and makes them remember my brand & optimistic personality when i walk out the door.

```html
<!DOCTYPE html>
<html lang="en">
<head>
<meta charset="utf-8">
<title>Tidecrest NZ – Business Card</title>
<link rel="stylesheet" href="https://fonts.googleapis.com/css2?family=Montserrat:wght@300;400;600;700&display=swap">
<style>
  :root {
    --page: #e4e5e7;
    --card: #2a2b2d;
    --card-deep: #222325;
    --accent: #1f9ad6;
    --text-soft: #b9bbbe;
    --text-muted: #8d9094;
    --pattern: #323335;
  }
  * { margin: 0; padding: 0; box-sizing: border-box; }
  html, body { width: 1200px; height: 847px; overflow: hidden; }
  body {
    background: var(--page);
    font-family: "Montserrat", sans-serif;
    position: relative;
  }
  .card {
    position: absolute;
    left: 290px;
    width: 620px;
    height: 354px;
    background: var(--card);
    border-bottom: 5px solid var(--accent);
    box-shadow: 0 6px 18px rgba(0,0,0,.18);
    overflow: hidden;
  }
  .card--back { top: 28px; }
  .card--front { top: 412px; }

  /* back side */
  .back-pattern {
    position: absolute; inset: 0;
    background: linear-gradient(135deg, var(--pattern), var(--card-deep));
  }
  .back-mark {
    position: absolute;
    left: 0; right: 0; top: 155px;
    display: flex; align-items: center; justify-content: center; gap: 12px;
    color: var(--accent);
    font-weight: 600;
    font-size: 30px;
    letter-spacing: 3px;
  }
  .mark-dot {
    width: 22px; height: 22px; border-radius: 50%;
    background: var(--accent);
  }

  /* front side */
  .brand {
    position: absolute; left: 42px; top: 118px;
  }
  .brand-name {
    display: flex; align-items: center; gap: 10px;
    color: var(--accent);
    font-weight: 600;
    font-size: 34px;
    letter-spacing: 2px;
    text-transform: uppercase;
    line-height: 1;
  }
  .brand-name .mark-dot { width: 20px; height: 20px; }
  .brand-services {
    margin-top: 8px;
    color: var(--text-muted);
    font-size: 10.5px;
    letter-spacing: .4px;
    text-transform: uppercase;
  }
  .divider {
    position: absolute; left: 352px; top: 92px;
    width: 2px; height: 150px;
    background: var(--accent);
  }
  .contact { position: absolute; left: 374px; top: 96px; }
  .person-name {
    color: var(--accent); font-weight: 700; font-size: 23px;
  }
  .person-role {
    color: var(--text-soft); font-weight: 400; font-size: 16px; margin: 2px 0 12px;
  }
  .contact-list { list-style: none; }
  .contact-list li {
    display: flex; align-items: center; gap: 9px;
    color: var(--text-soft); font-size: 15px; font-weight: 300; line-height: 25px;
  }
  .contact-list svg { width: 13px; height: 13px; fill: var(--accent); flex: none; }
  .social {
    position: absolute; left: 222px; top: 236px;
    display: flex; gap: 5px;
  }
  .social span {
    width: 15px; height: 15px; border-radius: 3px; background: var(--accent);
  }
  .motto {
    position: absolute; left: 0; right: 0; top: 282px;
    text-align: center;
    color: var(--text-soft); font-weight: 300; font-size: 19px;
  }
</style>
</head>
<body>

<section class="card card--back" aria-label="Card back">
  <div class="back-pattern" role="img" aria-label="Subtle tonal repeating brand pattern across a dark charcoal surface"></div>
  <div class="back-mark"><span class="mark-dot"></span>Tidecrest NZ</div>
</section>

<section class="card card--front" aria-label="Card front">
  <div class="brand">
    <div class="brand-name"><span class="mark-dot"></span>Tidecrest NZ</div>
    <div class="brand-services">Brand | Revenue | Events &amp; Promotions</div>
  </div>

  <div class="divider"></div>

  <div class="contact">
    <div class="person-name">Petra Ollingham</div>
    <div class="person-role">Director</div>
    <ul class="contact-list">
      <li>
        <svg viewBox="0 0 24 24" aria-hidden="true"><path d="M6.6 10.8a15 15 0 0 0 6.6 6.6l2.2-2.2a1 1 0 0 1 1-.25 11.4 11.4 0 0 0 3.6.57 1 1 0 0 1 1 1V20a1 1 0 0 1-1 1A17 17 0 0 1 3 4a1 1 0 0 1 1-1h3.5a1 1 0 0 1 1 1c0 1.25.2 2.45.57 3.57a1 1 0 0 1-.25 1z"/></svg>
        022 587 3091
      </li>
      <li>
        <svg viewBox="0 0 24 24" aria-hidden="true"><path d="M2 5h20v14H2z M2 5l10 8 10-8" fill="none" stroke="#1f9ad6" stroke-width="2.4"/></svg>
        petra@tidecrest.nz
      </li>
      <li>
        <svg viewBox="0 0 24 24" aria-hidden="true"><circle cx="12" cy="12" r="10" fill="none" stroke="#1f9ad6" stroke-width="2.4"/><path d="M2 12h20M12 2c3 3 3 17 0 20M12 2c-3 3-3 17 0 20" fill="none" stroke="#1f9ad6" stroke-width="1.8"/></svg>
        www.tidecrest.nz
      </li>
    </ul>
  </div>

  <div class="social" role="img" aria-label="Social media links">
    <span></span><span></span><span></span>
  </div>

  <p class="motto">Do what you love, love what you do</p>
</section>

</body>
</html>
```